Sales Training Power Point Presentation

We are looking for a power point presentation that allows us to turn our training manual into a presentation. I am attaching the training manual here, just to give an idea of what we will be presenting. We want to be able to have graphs for some of that data and be able to move around slides/edit as we see it is needed.

Target Market(s)

new sales employees

Industry/Entity Type

staffing

Colors
0054AA
0677BA
7BADD7
CADEEF
E8F1F8
F0912C
F2A743
F7CA91
FBE8D2
FDF5EE

Requirements
Must have
• graphs

```html
<!DOCTYPE html>
<html lang="en">
<head>
<meta charset="utf-8">
<title>Vantor Group – Sales Training Deck</title>
<link href="https://fonts.googleapis.com/css2?family=Montserrat:wght@400;500;600;700;800;900&family=Didact+Gothic&display=swap" rel="stylesheet">
<style>
:root{
  --orange:#ef7636;
  --orange-soft:#f2a743;
  --ink:#2c3036;
  --navy:#2d3a4c;
  --text:#3b3b3b;
  --muted:#6a6a6a;
  --stage-top:#c1c8ca;
  --stage:#e9e9e9;
  --white:#ffffff;
}
*{margin:0;padding:0;box-sizing:border-box}
html,body{width:1200px;height:2278px;overflow:hidden}
body{position:relative;background:var(--stage);font-family:"Didact Gothic",sans-serif;color:var(--text)}
.stage-top{position:absolute;left:0;top:0;width:1200px;height:793px;background:var(--stage-top)}

.slide{position:absolute;width:520px;height:388px;background:var(--white);overflow:hidden;box-shadow:0 18px 22px -12px rgba(0,0,0,.28)}
.slide p{font-size:7.2px;line-height:9.8px;text-align:justify;margin-bottom:9.5px}
.abs{position:absolute}

.head{position:absolute;left:22px;top:22px;display:flex;align-items:center;gap:10px}
.head-dot{width:30px;height:30px;border-radius:50%;background:var(--orange);border:3px solid #fff;box-shadow:0 1px 3px rgba(0,0,0,.3);flex:none;color:#fff;font:700 13px "Montserrat",sans-serif;display:flex;align-items:center;justify-content:center}
.head-title{font:800 21px "Montserrat",sans-serif;color:var(--ink);letter-spacing:-.2px;border-bottom:1.5px solid var(--orange);padding-bottom:3px;white-space:nowrap}
.head-title em{font-style:normal;color:var(--orange)}
.body{position:absolute;left:42px;right:44px;top:80px}

.footer{position:absolute;left:44px;right:14px;top:357px;display:flex;align-items:center;gap:8px}
.footer .url{font:500 5.6px "Montserrat",sans-serif;color:var(--ink)}
.footer .rule{flex:1;height:1px;background:var(--orange)}
.footer .num{width:12px;height:12px;border-radius:50%;background:var(--orange);color:#fff;font:700 6px "Montserrat",sans-serif;display:flex;align-items:center;justify-content:center}
.footer .brand{display:flex;flex-direction:column;align-items:center;gap:1px;font:600 5.4px "Montserrat",sans-serif;color:var(--navy);letter-spacing:.4px;white-space:nowrap}
.footer .brand i{width:8px;height:8px;border-radius:50%;background:var(--orange);display:block}

.toc-dot{position:absolute;left:27px;top:19px;width:44px;height:44px;border-radius:50%;background:var(--orange);border:4px solid #fff;box-shadow:0 1px 4px rgba(0,0,0,.35);z-index:2}
.toc-pill{position:absolute;left:60px;top:24px;width:355px;height:33px;background:var(--ink);border-radius:0 18px 18px 0;color:#fff;font:500 25px "Montserrat",sans-serif;padding-left:28px;line-height:34px;letter-spacing:.3px;white-space:nowrap}
.toc-line{position:absolute;left:415px;top:40px;width:76px;height:1.5px;background:var(--orange)}
.toc-line::after{content:"";position:absolute;right:-3px;top:-3px;width:7px;height:7px;border-radius:50%;background:var(--orange)}
.toc-group{position:absolute;width:215px}
.toc-main{display:flex;align-items:baseline;font:500 7.4px "Montserrat",sans-serif;color:var(--ink);position:relative;white-space:nowrap}
.toc-main::before{content:"";position:absolute;left:-12px;top:1px;width:7px;height:7px;border-radius:50%;background:var(--orange)}
.toc-main .lead{flex:1;border-bottom:1px dotted #777;margin:0 2px 2px}
.toc-sub{margin:8px 0 0 13px;font-size:7px;line-height:10.6px;color:var(--muted)}
.toc-band{position:absolute;left:0;bottom:0;width:520px;height:60px;background:var(--orange)}
.toc-brand{position:absolute;right:28px;top:12px;display:flex;flex-direction:column;align-items:center;gap:6px;color:#fff;font:600 9.5px "Montserrat",sans-serif;letter-spacing:1.2px;white-space:nowrap}
.toc-brand i{width:18px;height:18px;border-radius:50%;background:#fff;display:block}

.ind-label{position:absolute;font:700 10px "Montserrat",sans-serif;color:var(--ink);line-height:13px}
.ind-label span{display:block;font:400 10px "Didact Gothic",sans-serif;color:var(--muted)}

.col-left{position:absolute;left:42px;top:26px;width:206px}
.col-right{position:absolute;left:276px;top:28px;width:206px}
.divider{position:absolute;left:258px;top:18px;width:1px;height:322px;background:#cfcfcf}
.small{font-size:7.2px;line-height:9.4px}
.niche{display:grid;grid-template-columns:70px 78px 60px;row-gap:5px;margin-top:9px;font:600 7.2px "Montserrat",sans-serif;color:var(--ink)}
.niche span::before{content:"";display:inline-block;width:4px;height:4px;border-radius:50%;background:var(--orange);margin-right:6px;vertical-align:1px}
.hr{height:1px;background:#bfbfbf}
.tag{display:inline-block;background:var(--orange);color:#fff;font:800 7.2px "Montserrat",sans-serif;padding:1px 3px}
.strong{font-family:"Montserrat",sans-serif;font-size:6.8px;font-weight:500}

.cover{position:absolute;left:280px;top:158px;width:640px;height:477px;background:#fff;overflow:hidden;box-shadow:0 24px 30px -14px rgba(0,0,0,.3)}
.cover-brand{position:absolute;left:38px;top:40px;display:flex;flex-direction:column;align-items:center;gap:10px;font:500 19px "Montserrat",sans-serif;color:var(--navy);letter-spacing:2.2px;white-space:nowrap}
.cover-brand i{width:34px;height:34px;border-radius:50%;background:var(--orange);display:block}
.cover-title{position:absolute;left:38px;top:344px;font:900 40px/37px "Montserrat",sans-serif;color:var(--ink)}
.cover-title em{display:block;font-style:normal;color:var(--orange)}
.cover-rule{position:absolute;left:38px;top:432px;width:210px;height:1.5px;background:var(--ink)}
.cover-url{position:absolute;left:38px;top:440px;font:500 11px "Montserrat",sans-serif;color:var(--ink);letter-spacing:.5px}

.logo-block{position:absolute;left:680px;top:1920px;width:400px;display:flex;flex-direction:column;align-items:center;gap:30px}
.logo-block i{width:76px;height:76px;border-radius:50%;background:var(--orange);display:block}
.logo-block b{font:600 36px "Montserrat",sans-serif;color:var(--navy);letter-spacing:4px;white-space:nowrap}
</style>
</head>
<body>

<div class="stage-top"></div>

<section class="cover">
  <svg class="abs" style="left:0;top:0" width="640" height="477" viewBox="0 0 640 477">
    <defs>
      <linearGradient id="skyGrad" x1="0" y1="0" x2="0" y2="1">
        <stop offset="0" stop-color="#3f7fc4"/>
        <stop offset=".55" stop-color="#9cc3e6"/>
        <stop offset="1" stop-color="#5d7f9c"/>
      </linearGradient>
    </defs>
    <ellipse cx="480" cy="250" rx="232" ry="262" fill="none" stroke="var(--orange)" stroke-width="10" stroke-dasharray="420 2000" stroke-dashoffset="-560"/>
    <ellipse cx="490" cy="244" rx="226" ry="258" fill="url(#skyGrad)" role="img" aria-label="Photo: smiling businesswoman holding a tablet in front of a glass office building under a blue sky"/>
  </svg>
  <div class="cover-brand"><i></i>VANTOR GROUP</div>
  <div class="cover-title">SALES<em>TRAINING</em></div>
  <div class="cover-rule"></div>
  <div class="cover-url">WWW.VANTORGROUP.COM</div>
</section>

<section class="slide" style="left:49px;top:858px">
  <div class="toc-dot"></div>
  <div class="toc-pill">TABLE OF CONTENTS</div>
  <div class="toc-line"></div>

  <div class="toc-group" style="left:38px;top:85px">
    <div class="toc-main">INDUSTRY ACUMEN<span class="lead"></span>5</div>
    <div class="toc-sub">Contract Staffing<br>Full Time Staffing<br>Project Based Objectives<br>Project Outsourcing vs. Contract Staffing<br>Opportunity Recognition</div>
  </div>
  <div class="toc-group" style="left:38px;top:174px">
    <div class="toc-main">VANTOR TECHNOLOGY:VALUE PROPOSITION<span class="lead"></span>9</div>
    <div class="toc-sub">Defining VANTOR'S Value Proposition<br>Defining YOUR Value Proposition<br>Accomplishing Value Proposition<br>Proving Value Proposition</div>
  </div>
  <div class="toc-group" style="left:38px;top:251px">
    <div class="toc-main">SALES CYCLE<span class="lead"></span>16</div>
    <div class="toc-sub">Prospecting<br>Account Penetration<br>Obtaining Business<br>Account Retention</div>
  </div>

  <div class="toc-group" style="left:293px;top:85px;width:200px">
    <div class="toc-main">DAILY SALES ACTIVITY<span class="lead"></span>45</div>
    <div class="toc-sub">"To Do" List<br>Client Strategy<br>Current Market Activity<br>Communication Model<br>Cold Call / Leads</div>
  </div>
  <div class="toc-group" style="left:293px;top:174px;width:200px">
    <div class="toc-main">SYSTEMS &amp; TOOLS<span class="lead"></span>48</div>
    <div class="toc-sub">Mailroom<br>PlaceTrack<br>Web</div>
  </div>
  <div class="toc-group" style="left:293px;top:251px;width:194px">
    <div class="toc-main">BUSINESS PLANS<span class="lead"></span>56</div>
  </div>

  <div class="toc-band">
    <div class="toc-brand"><i></i>VANTOR GROUP</div>
  </div>
</section>

<section class="slide" style="left:616px;top:858px">
  <div class="head"><span class="head-dot"></span><h2 class="head-title">SALES TRAINING <em>INTRODUCTION:</em></h2></div>
  <div class="body">
    <p>Welcome to Vantor Technology's training guide to sales. We are very excited that you have joined our sales team. A career in sales is a worthwhile pursuit and our goal is to better arm you for success. We certainly believe our services are among the best in the industry and plan on continuing this legacy through the techniques outlines in this training course</p>
    <p>The following pages will provide a detailed outline of industry acumen, Vantor's Value Proposition, Sales Cycle, Sales Activity, Systems / Tools, the construction of an individual business plan. These items represent the core of our beliefs in establishing a sales career founded on good principles and a drive toward professional success.</p>
    <p>Selling is defined by Lexford as: to exchange a product or service for money; offer for sale. It is very important that you keep this principle in mind at all times. There are many varied techniques, systems, and processes we use to deliver top-notch services. However, all are geared toward one ultimate end, to generate a profit…to make money.</p>
    <p>As you may imagine the processes and techniques required to excel in sales are somewhat more complex than Lexford's definition implies. Throughout this training program we will explore both general sales techniques as well as techniques unique to Vantor.</p>
    <p>The business world continues to evolve around us. A well-trained sales professional sees this evolution or change as opportunity. This manual is designed to arm you with the skills, product knowledge, and business focus needed to capitalize on these opportunities within the marketplace. The most important tool being product / service knowledge. As a finely tuned sales professional, you must possess a deep understanding of your product / service and its capabilities. We explore a number of ways to utilize our products to a client's advantage so you can be prepared. Flexibility plays a key role in providing quality products and services, flexibility starts with a detailed understanding of our business and the variety of solutions we provide.</p>
  </div>
  <div class="footer"><span class="url">WWW.VANTORGROUP.COM</span><span class="rule"></span><span class="num">3</span><span class="rule"></span><span class="brand"><i></i>VANTOR GROUP</span></div>
</section>

<section class="slide" style="left:49px;top:1322px">
  <div class="head"><span class="head-dot"></span><h2 class="head-title">SALES TRAINING <em>INTRODUCTION:</em></h2></div>
  <div class="body" style="top:75px">
    <p>There are certain sales principles that will prove successful regardless of your background, market knowledge, competition, or tenure in the industry. Throughout this course we will make a concerted effort toward becoming experts in the techniques that have yielded success time and time again. We consider that foundation critical to your success both short and long-term.</p>
    <p>The ever-increasing reliance of businesses on computers and technology, much like many other industries, has changed the occupation of sales forever. The availability of information has made our job easier in some ways, leveled the competitive playing field in others, but generally has brought the world together in ways never imagined. We will explore new and improved ways of utilizing this technology to the max. Staying ahead of the technology curve with cutting edge sales tools and improved techniques is Vantor's commitment to our sales force.</p>
    <p>Finally, we assist you in creating a map for success or Business Plan. This map begins with a self-appraisal of your knowledge in the core competencies of the job and ends with a completed game plan delivering you to a desired destination of success. We provide direction in each stage of the Business Plan creation and continue through execution. This Business Plan is designed to help you stay the course through what will certainly be an action packed first year on the job.</p>
    <p>The sales profession is a wonderful career. As stated previously, the business environment is ever changing and will provide you with some extremely difficult, yet rewarding, challenges. Thus, being prepared with a great understanding of what we sell, who buys it, and how to manage your business relationships is critical to your success. Welcome to Vantor! Good Luck!</p>
  </div>
  <div class="footer"><span class="url">WWW.VANTORGROUP.COM</span><span class="rule"></span><span class="num">4</span><span class="rule"></span><span class="brand"><i></i>VANTOR GROUP</span></div>
</section>

<section class="slide" style="left:616px;top:1322px">
  <div class="head"><span class="head-dot">1</span><h2 class="head-title" style="border:0">INDUSTRY ACUMEN:</h2></div>
  <div class="body" style="top:76px">
    <p>For over a century the staffing industry has been called upon to help employers locate employees and vise/versa. As time has passed and business has grown more and more complex, staffing companies have both increased their size and scope. Now, the professional services or staffing industry has been touted as one of the fastest growing sectors in the business community. After many years of being almost exclusively linked to low level temp positions and general laborers, recruitment firms can now be found in 85% of the total job market. The following outlines some additional fact and figures:</p>
  </div>
  <div class="abs small" style="right:50px;top:157px;color:var(--text)">The Staffing Industry is made up of the following types of firms:</div>

  <svg class="abs" style="left:22px;top:175px" width="160" height="165" viewBox="0 0 160 165">
    <path d="M12 110 A68 68 0 0 0 130 140" fill="none" stroke="var(--orange)" stroke-width="6"/>
    <circle cx="80" cy="80" r="68" fill="#6d7f93" role="img" aria-label="Photo: engineer in a hard hat holding blueprints and pointing at a site"/>
  </svg>

  <svg class="abs" style="left:300px;top:200px" width="100" height="100" viewBox="0 0 100 100">
    <path d="M50 12 A38 38 0 0 1 88 50" fill="none" stroke="#2b2b2b" stroke-width="12"/>
    <path d="M88 50 A38 38 0 0 1 50 88" fill="none" stroke="#111" stroke-width="12"/>
    <path d="M50 88 A38 38 0 0 1 12 50" fill="none" stroke="#9a9a9a" stroke-width="12"/>
    <path d="M12 50 A38 38 0 0 1 50 12" fill="none" stroke="#6e6e6e" stroke-width="12"/>
    <circle cx="50" cy="50" r="22" fill="var(--orange)"/>
    <g font-family="Montserrat" font-weight="700" font-size="7" text-anchor="middle">
      <circle cx="66" cy="15" r="6" fill="#fff"/><text x="66" y="17.5">2</text>
      <circle cx="85" cy="66" r="6" fill="#fff"/><text x="85" y="68.5">1</text>
      <circle cx="15" cy="34" r="6" fill="#fff"/><text x="15" y="36.5">3</text>
      <circle cx="34" cy="85" r="6" fill="#fff"/><text x="34" y="87.5">4</text>
    </g>
  </svg>

  <div class="ind-label" style="left:242px;top:205px">Direct<br>Placement<br>Firms</div>
  <div class="ind-label" style="right:56px;top:205px;text-align:right">Contract<br>Services<br>Firm</div>
  <div class="ind-label" style="left:242px;top:270px">Blended<br>Services<span>(Contract / Direct<br>Placement Firms)</span></div>
  <div class="ind-label" style="right:56px;top:270px;text-align:right">Executive<br>Search Firms<span>(Retained Search)</span></div>

  <div class="footer"><span class="url">WWW.VANTORGROUP.COM</span><span class="rule"></span><span class="num">5</span><span class="rule"></span><span class="brand"><i></i>VANTOR GROUP</span></div>
</section>

<section class="slide" style="left:49px;top:1781px">
  <div class="divider"></div>
  <div class="col-left">
    <div class="small">These staffing organizations may be generalists or can specialize in a specific placement niche such as:</div>
    <div class="niche"><span>Office</span><span>Industrial</span><span>Trades</span><span>Legal</span><span>Technical</span><span>Medical</span><span>Home Care</span><span style="grid-column:span 2">Specialized Executive Search</span></div>
    <div class="hr" style="margin:16px -6px 0"></div>
    <div role="img" aria-label="Map of the United States" style="position:relative;margin:11px 0 0 15px;width:157px;height:96px;background:var(--orange);border-radius:18px 30px 40px 22px;color:#fff;font:800 26px 'Montserrat',sans-serif;padding:22px 0 0 34px;line-height:24px"><span style="display:block;font:400 7px 'Didact Gothic',sans-serif">In the</span>USA</div>
    <div class="small" style="text-align:center;margin-top:18px">the first employment agencies were founded in</div>
    <div style="font:800 19px 'Montserrat',sans-serif;color:var(--ink);text-align:center;margin-top:1px;white-space:nowrap">THE LATE 1800'S</div>
    <div style="font:700 11px 'Montserrat',sans-serif;color:var(--ink);margin:18px 0 0 2px">They include:</div>
    <div class="small" style="margin-left:2px;color:var(--text);font-size:6.8px;line-height:8.6px"><span style="color:var(--orange);font-size:7.6px">The Labor Exchange 1880 &amp; Builders Agency</span> (now Summit Employment Group/Ridge Personnel) 1893.</div>
  </div>

  <div class="col-right">
    <span class="tag">WHILE YEARS BACK,</span>
    <div class="strong">employment agency (direct) placement fees were primarily paid for by the applicant (candidate).</div>
    <span class="tag" style="margin-top:10px">TODAY,</span>
    <div class="strong">the client companies pay most all employment agencies fees.<b>(Average direct placement fee: 25% of candidate's annual salary)</b></div>
    <div class="hr" style="margin:18px -6px 0"></div>
    <div style="display:flex;gap:8px;margin-top:14px;align-items:flex-start">
      <svg width="18" height="18" viewBox="0 0 18 18"><circle cx="9" cy="6" r="4" fill="var(--orange)"/><path d="M2 18 a7 6 0 0 1 14 0z" fill="var(--orange)"/></svg>
      <div><div style="font:700 9px 'Montserrat',sans-serif;color:var(--ink)">The temporary help service industry</div><div class="small" style="color:var(--muted)">has the majority of customers.</div></div>
    </div>
    <div style="display:flex;align-items:center;gap:14px;margin-top:20px">
      <div style="font:500 7px 'Montserrat',sans-serif;color:var(--ink)">In 2018, revenues<br>in staffing were</div>
      <div style="background:var(--orange);color:#fff;font:800 16px 'Montserrat',sans-serif;padding:3px 6px;white-space:nowrap">$167 Billion</div>
    </div>
    <div class="hr" style="margin:16px -6px 0"></div>
    <div style="font:500 6.8px 'Montserrat',sans-serif;color:var(--ink);margin-top:18px">According to the National Staffing Council,</div>
    <div style="font:900 35px/34px 'Montserrat',sans-serif;color:var(--orange);white-space:nowrap">OVER 90%</div>
    <div style="font:500 7px 'Montserrat',sans-serif;color:var(--ink)">of USA companies utilize temporary help.</div>
  </div>
  <div class="footer"><span class="url">WWW.VANTORGROUP.COM</span><span class="rule"></span><span class="num">6</span><span class="rule"></span><span class="brand"><i></i>VANTOR GROUP</span></div>
</section>

<div class="logo-block"><i></i><b>VANTOR GROUP</b></div>

</body>
</html>
```